Residential technology services web site

We are looking for a web design to represent our new company which provides RESIDENTIAL technology services, such as computer and tablet repair, maintenance, networking, training, etc (like FixCrew).
We are an upbeat, fun, professional organization that provides premium services to residential clients. Because the focus is on residential clients, the design should be modern (a little web2.0ish), easy to navigate, come off a little fun, but still inspire confidence that we are professionals who will get the job done right.
We are looking for four pages:
-home page
-services page highlighting some of the more common services
-about page
-template page that can be used to showcase each specific service in greater detail
Some sample sites:
laptop-mender-harbor.example - layout
sparkfixmaple - layout
helpowls.example - great site
pcvalor.example - layout
devicefix-athome.example
Home page should promote PC repair, Mac repair, tablet screen repair, tablet/computer training, pick up and delivery, mission statement, parental controls, wireless networking setup, computer hookups, anything else you think is enticing. Does not have to be all the above services, could use slider for select few. Non service items have to be included. Discreet twitter/fb social buttons. Discreet testimonial section (1-2 testimonials). If I think of more stuff I will add, or you can use your imagination. Ways to get service, phone, remote, onsite, in lab.
Should also mention xx% off for new customers
One of the slides should be our guarantee to customers.
Services page should highlight some common services and show ways of getting them (onsite, phone, remote). Other than highlighting select few it should also link to each of our other services. Add other stuff as you see necessary.
Template page for each service should display one service, list what a customer will receive with the service, and have three columns for price (remote, onsite, lab). Also have linkbacks to other services. FixCrews service page is a good example (but shouldn't be a replica): http://www.fixcrew.example/services/computers-networking/email-setup.aspx
About us page is just that, mission statement, place for us to type up our service pledge/guarantee, some other stuff if you can think of it.
You can use placeholder text for now. Feel free to use stock images if you must, I will buy them afterwards, you should really only need a couple at most.
Header should have logo obviously, which I will upload here. Call to action: "Bite Back!" and list phone number. A menu: Home Services About - make sure to make it so more buttons could be added later.
Footer should have the obvious, maybe mini menu, copyright, mission statement, link to privacy policy, etc.
After selecting a style/submission we like, we can go into more specifics for each page.
If I'm doing this project thing wrong, please let me know!
Target Market(s)
Inexperience computer users, tablet users, those unable to do own repairs
Industry/Entity Type
Residential
Requirements
Nice to have
- We want the website to be catchy and utilize our colors along with a generous amount of black. Don't want the site to be too light/white.

```html
<!DOCTYPE html>
<html lang="en">
<head>
<meta charset="utf-8">
<title>ByteMend – Services</title>
<link href="https://fonts.googleapis.com/css2?family=Source+Sans+3:wght@400;600;700&display=swap" rel="stylesheet">
<style>
:root{
  --green:#7dc242;
  --green-light:#a6d66a;
  --green-dark:#5a9e2a;
  --black:#111;
  --hero:#1a1a1a;
  --grey-card:#f1f1f1;
  --text:#666;
  --title:#3a3a3a;
  --link-blue:#1d62a8;
  --footer:#2b2b2b;
  --white:#fff;
}
*{margin:0;padding:0;box-sizing:border-box}
html,body{width:817px;height:1200px;overflow:hidden;background:var(--white)}
body{position:relative;font-family:"Source Sans 3",Arial,sans-serif;color:var(--text)}
.abs{position:absolute}
.top-rule{left:0;top:0;width:817px;height:4px;background:var(--green)}
.brand{left:83px;top:34px;display:flex;align-items:center;gap:8px;font-size:30px;font-weight:700;color:var(--black)}
.brand-mark{width:18px;height:18px;background:var(--green)}
.nav{left:0;top:4px;height:36px;font-size:10.5px;color:#222}
.nav a{position:absolute;top:0;height:36px;line-height:36px;text-decoration:none;color:#222;padding:0 14px}
.nav a.active{background:var(--green)}
.call{left:528px;top:70px;font-size:20px;font-weight:700;color:var(--black);white-space:nowrap}
.call span{color:var(--green)}
.band{left:0;width:817px;height:6px;background:var(--green)}
.hero{left:0;top:108px;width:817px;height:296px;background:radial-gradient(ellipse at 55% 40%,#3a3a3a 0%,#1a1a1a 55%,#0d0a0a 100%)}
.hero h1{position:absolute;left:90px;top:18px;font-size:26px;font-weight:700;color:var(--white);white-space:nowrap}
.hero .sub{position:absolute;left:90px;top:48px;font-size:19px;color:var(--white)}
.hero ul{position:absolute;left:100px;top:93px;list-style:none}
.hero li{font-family:Arial,sans-serif;font-size:10.5px;color:#e8e8e8;height:22.4px;padding-left:15px;position:relative}
.hero li::before{content:"";position:absolute;left:0;top:3px;width:6px;height:6px;border-radius:50%;background:var(--green)}
.btn{position:absolute;display:block;text-align:center;font-size:10px;font-weight:700;text-decoration:none}
.btn-black{background:var(--black);color:var(--white)}
.btn-green{background:var(--green);color:var(--white);font-weight:600}
.hero .btn{top:245px;height:23px;line-height:23px}
.arrow{position:absolute;top:124px;width:26px;height:26px}
.hero-art{position:absolute;left:299px;top:62px;width:444px;height:234px;background:radial-gradient(ellipse at 60% 60%,rgba(125,194,66,.35),rgba(125,194,66,0) 70%)}
.dots{left:362px;top:419px;display:flex;gap:10.5px}
.dots i{width:10px;height:10px;border-radius:50%;background:#ccc}
.dots i.on{background:var(--green)}
.service{position:absolute;left:71px;width:404px;height:133px}
.service.grey{background:var(--grey-card)}
.service::after{content:"";position:absolute;left:0;bottom:-1px;width:404px;height:2px;background:linear-gradient(90deg,transparent,var(--green) 15%,var(--green) 85%,transparent)}
.service .icon{position:absolute;left:12px;top:22px;width:75px;height:52px;border-radius:6px;background:linear-gradient(#7dc242,#1a1a1a)}
.service h2{position:absolute;left:96px;top:14px;font-size:20px;font-weight:700;color:var(--title);white-space:nowrap}
.service p{position:absolute;left:96px;top:45px;width:290px;font-family:Arial,sans-serif;font-size:7.3px;line-height:10.3px;color:#777}
.service .btn{top:88px;height:23px;line-height:23px}
.side{position:absolute;left:514px;width:203px;border-radius:6px}
.free{top:446px;height:104px;background:linear-gradient(#2a2a2a,#0d0d0d);color:var(--white)}
.free h3{position:absolute;left:23px;top:13px;font-size:13.5px;font-weight:600;line-height:17px}
.free h3 b{color:var(--green);font-size:16px}
.free .btn{left:23px;top:63px;width:72px;height:23px;line-height:23px}
.free .art{position:absolute;left:122px;top:48px;width:75px;height:62px;border-radius:6px;background:linear-gradient(135deg,#7dc242,#c49a6c)}
.pack{height:171px;background:linear-gradient(#7dc242,#a9d86e);color:var(--white)}
.pack h3{position:absolute;left:23px;top:18px;font-size:13px;font-weight:600;line-height:17px}
.pack h3 b{color:#333;font-size:16px;font-weight:700}
.pack ul{position:absolute;left:23px;top:68px;list-style:none}
.pack li{font-size:10.5px;font-weight:700;color:var(--link-blue);height:15px;padding-left:10px;position:relative}
.pack li::before{content:"";position:absolute;left:0;top:5px;width:5px;height:5px;border-radius:50%;background:var(--black)}
.pack .btn{left:109px;top:139px;width:84px;height:23px;line-height:23px}
.footer{left:0;top:1142px;width:817px;height:58px;background:var(--footer);font-size:9px;color:#aaa}
.footer .mark{position:absolute;left:71px;top:12px;width:56px;height:34px;border-radius:4px;background:linear-gradient(#7dc242,#1a1a1a)}
.footer .social{position:absolute;top:17px;width:22px;height:22px;border-radius:50%;background:var(--green)}
.footer .links{position:absolute;left:375px;top:23px;white-space:nowrap}
.footer .links span{margin:0 8px}
.footer .copy{position:absolute;left:676px;top:23px}
</style>
</head>
<body>
<div class="abs top-rule"></div>

<header>
  <div class="abs brand"><span class="brand-mark"></span>ByteMend</div>
  <nav class="abs nav">
    <a style="left:417px">HOME</a>
    <a class="active" style="left:491px">SERVICES</a>
    <a style="left:579px">ABOUT</a>
    <a style="left:651px">SOMETHING</a>
  </nav>
  <div class="abs call"><span>Bite back</span> (619) 555 0182</div>
</header>

<div class="abs band" style="top:102px"></div>
<section class="abs hero">
  <h1>Our Repair &amp; Maintenance Services</h1>
  <p class="sub">Lorem ipsum 30% today!</p>
  <ul>
    <li>Adipiscing elit lorem</li>
    <li>Ipsum dolor sit amet consectetur</li>
    <li>Adipiscing elit lorem ipsum</li>
    <li>Dolor sit amet</li>
    <li>Consectetur adipiscing elit.</li>
    <li>Adipiscing elit lorem ipsum</li>
  </ul>
  <a class="btn btn-black" style="left:98px;width:85px">Compare Deals</a>
  <a class="btn btn-green" style="left:194px;width:85px">Order Now</a>
  <div class="hero-art" role="img" aria-label="Illustration of cheerful green gadget characters: tablet, laptop, desktop tower, monitor, phones and game controller"></div>
  <svg class="arrow" style="left:43px" viewBox="0 0 26 26"><circle cx="13" cy="13" r="13" fill="#ccc"/><path d="M15 7l-6 6 6 6" stroke="#333" stroke-width="3" fill="none"/></svg>
  <svg class="arrow" style="left:748px" viewBox="0 0 26 26"><circle cx="13" cy="13" r="13" fill="#ccc"/><path d="M11 7l6 6-6 6" stroke="#333" stroke-width="3" fill="none"/></svg>
</section>
<div class="abs band" style="top:404px"></div>

<div class="abs dots"><i class="on"></i><i></i><i></i><i></i><i></i></div>

<main>
  <article class="service grey" style="top:446px">
    <div class="icon" role="img" aria-label="Green laptop character icon"></div>
    <h2>Laptop Repair</h2>
    <p>Lorem ipsum dolor sit amet consectetur quid adipiscing elit, sit amet et quid consectetur. Lorem ipsum dolor sit amet consectetur alead adipiscing elit, sit amet et quid consectetur elit adipiscing dolor ipsum.</p>
    <a class="btn btn-green" style="left:96px;width:72px">Learn more</a>
    <a class="btn btn-black" style="left:171px;width:80px">Order Now</a>
  </article>
  <article class="service" style="top:579px">
    <div class="icon" role="img" aria-label="Green tablet character icon"></div>
    <h2>Tablet Repair</h2>
    <p>Lorem ipsum dolor sit amet consectetur quid adipiscing elit, sit amet et quid consectetur. Lorem ipsum dolor sit amet consectetur alead adipiscing elit, sit amet et quid consectetur elit adipiscing dolor ipsum.</p>
    <a class="btn btn-green" style="left:96px;width:72px">Learn more</a>
    <a class="btn btn-black" style="left:171px;width:80px">Order Now</a>
  </article>
  <article class="service grey" style="top:712px">
    <div class="icon" role="img" aria-label="Two green smartphone character icons"></div>
    <h2>Smartphone Repair</h2>
    <p>Lorem ipsum dolor sit amet consectetur quid adipiscing elit, sit amet et quid consectetur. Lorem ipsum dolor sit amet consectetur alead adipiscing elit, sit amet et quid consectetur elit adipiscing dolor ipsum.</p>
    <a class="btn btn-green" style="left:96px;width:72px">Learn more</a>
    <a class="btn btn-black" style="left:171px;width:80px">Order Now</a>
  </article>
  <article class="service" style="top:847px">
    <div class="icon" role="img" aria-label="Desktop tower and monitor character icons"></div>
    <h2>Desktop Repair</h2>
    <p>Lorem ipsum dolor sit amet consectetur quid adipiscing elit, sit amet et quid consectetur. Lorem ipsum dolor sit amet consectetur alead adipiscing elit, sit amet et quid consectetur elit adipiscing dolor ipsum.</p>
    <a class="btn btn-green" style="left:96px;width:72px">Learn more</a>
    <a class="btn btn-black" style="left:171px;width:80px">Order Now</a>
  </article>
  <article class="service grey" style="top:981px">
    <div class="icon" role="img" aria-label="Green game controller character icon"></div>
    <h2>Game Console Repair</h2>
    <p>Lorem ipsum dolor sit amet consectetur quid adipiscing elit, sit amet et quid consectetur. Lorem ipsum dolor sit amet consectetur alead adipiscing elit, sit amet et quid consectetur elit adipiscing dolor ipsum.</p>
    <a class="btn btn-green" style="left:96px;width:72px">Learn more</a>
    <a class="btn btn-black" style="left:171px;width:80px">Order Now</a>
  </article>
</main>

<aside>
  <div class="side free">
    <h3><b>FREE</b> Pickup and Delivery<br>right to your door!</h3>
    <a class="btn btn-green">View Details</a>
    <div class="art" role="img" aria-label="Tablet character popping out of a delivery box"></div>
  </div>
  <div class="side pack" style="top:569px">
    <h3><b>BASIC</b> Tune-up &amp; Repair<br>Service Package Features</h3>
    <ul><li>Lorem ipsum dolor</li><li>Elit consectetur</li><li>Site amet</li><li>Adipiscing elit</li></ul>
    <a class="btn btn-black">Learn more</a>
  </div>
  <div class="side pack" style="top:759px">
    <h3><b>PREMIUM</b> Repair Service<br>Package Features</h3>
    <ul><li>Lorem ipsum dolor</li><li>Elit consectetur</li><li>Site amet</li><li>Adipiscing elit</li></ul>
    <a class="btn btn-black">Learn more</a>
  </div>
</aside>

<footer class="abs footer">
  <div class="mark" role="img" aria-label="Small laptop character"></div>
  <span class="social" style="left:137px" aria-label="Social link"></span>
  <span class="social" style="left:168px" aria-label="Social link"></span>
  <span class="social" style="left:199px" aria-label="Social link"></span>
  <div class="links">Privacy Policy<span>|</span>Sitemap</div>
  <div class="copy">Copyright 2012</div>
</footer>
</body>
</html>
```